Finance Product Agency Business Card Design

We're an agency that provides products (service contracts, gap insurance, tire and wheel, etc) and support to dealership finance departments. We specialize in training finance producers to maximize their potential and also keep them up to date on the ever changing compliance and legal landscape. I'll attach an image of our logo, excited to see what you all come up with. Would also be interested in discussing our new website design with the winner.

Target Market(s)

auto dealerships

Industry/Entity Type

Business

Contact Information for Business Card

Mark Dolvery
Phone 317.624.5583
Fax 855.472.3308
email Mark.Dolvery@brightlanecoverage.example

Requirements
Must have
• basic contact information
Nice to have
• looking for something professional but modern

```html
<!DOCTYPE html>
<html lang="en">
<head>
<meta charset="utf-8">
<title>Brightlane Coverage – Business Card</title>
<link rel="stylesheet" href="https://fonts.googleapis.com/css2?family=Open+Sans:wght@400;600&display=swap">
<style>
  :root {
    --backdrop: #ececec;
    --card-white: #ffffff;
    --card-dark: #2f2e2f;
    --accent-teal: #3e6f85;
    --logo-grey: #45474b;
    --text-light: #f2f2f2;
    --rule-light: #d9d9d9;
  }
  * { margin: 0; padding: 0; box-sizing: border-box; }
  html, body {
    width: 1200px; height: 800px; overflow: hidden;
    background: var(--backdrop);
    font-family: "Open Sans", Arial, sans-serif;
  }
  .sheet {
    position: relative; width: 1200px; height: 800px;
    display: flex; align-items: center; justify-content: center; gap: 40px;
  }
  .card {
    position: relative; width: 540px; height: 309px; overflow: hidden;
    box-shadow: 0 6px 18px rgba(0,0,0,0.18);
  }
  .card-shapes { position: absolute; inset: 0; }

  /* Logo lockup */
  .logo {
    position: absolute; display: flex; align-items: center; gap: 10px;
  }
  .logo-dot {
    width: 30px; height: 30px; border-radius: 50%;
    background: var(--accent-teal); flex: none;
  }
  .logo-name {
    font-weight: 600; font-size: 20px; line-height: 1.1;
    color: var(--logo-grey); text-transform: uppercase; letter-spacing: 0.5px;
  }

  /* Front */
  .card-front { background: var(--card-white); }
  .card-front .logo { left: 16px; top: 122px; }
  .contact {
    position: absolute; left: 222px; top: 96px; right: 16px;
    color: var(--text-light);
  }
  .contact-name {
    font-size: 21px; font-weight: 400; letter-spacing: 0.6px;
  }
  .contact-rule {
    width: 112px; height: 2px; background: var(--rule-light);
    margin: 8px 0 20px;
  }
  .contact-row {
    display: flex; align-items: center; gap: 20px;
    font-size: 10px; letter-spacing: 0.3px; margin-bottom: 9px;
  }
  .contact-item { display: flex; align-items: center; gap: 6px; }
  .contact-icon { width: 13px; height: 13px; flex: none; }

  /* Back */
  .card-back { background: var(--card-dark); }
  .back-band {
    position: absolute; left: 0; right: 0; top: 82px; height: 145px;
    background: var(--card-white);
  }
  .card-back .logo {
    left: 50%; top: 50%; transform: translate(-50%, -50%);
  }
  .card-back .logo-name { font-size: 24px; }
  .card-back .logo-dot { width: 34px; height: 34px; }
</style>
</head>
<body>
<main class="sheet">

  <section class="card card-front" aria-label="Business card front">
    <svg class="card-shapes" width="540" height="309" viewBox="0 0 540 309" aria-hidden="true">
      <polygon points="176,0 200,0 210,309 204,309" fill="var(--accent-teal)"/>
      <polygon points="198,0 540,0 540,309 210,309" fill="var(--card-dark)"/>
    </svg>

    <div class="logo">
      <span class="logo-dot"></span>
      <span class="logo-name">Brightlane<br>Coverage</span>
    </div>

    <div class="contact">
      <p class="contact-name">Mark Dolvery</p>
      <div class="contact-rule"></div>
      <div class="contact-row">
        <span class="contact-item">
          <svg class="contact-icon" viewBox="0 0 16 16" aria-label="Phone">
            <circle cx="8" cy="8" r="7" fill="none" stroke="currentColor" stroke-width="1.3"/>
            <path d="M5.6 4.6l1.2-.3.8 1.8-.9.7a5 5 0 0 0 2.5 2.5l.7-.9 1.8.8-.3 1.2c-3 .3-6.1-2.8-5.8-5.8z" fill="currentColor"/>
          </svg>
          317.624.5583
        </span>
        <span class="contact-item">
          <svg class="contact-icon" viewBox="0 0 16 16" aria-label="Fax">
            <circle cx="8" cy="8" r="7" fill="currentColor"/>
            <rect x="5.5" y="4" width="5" height="3" fill="var(--card-dark)"/>
            <rect x="4" y="7" width="8" height="4" rx="0.8" fill="var(--card-dark)"/>
          </svg>
          855.472.3308
        </span>
      </div>
      <div class="contact-row">
        <span class="contact-item">
          <svg class="contact-icon" viewBox="0 0 16 16" aria-label="Email">
            <circle cx="8" cy="8" r="7" fill="currentColor"/>
            <rect x="4" y="5.2" width="8" height="5.6" fill="var(--card-dark)"/>
            <path d="M4.3 5.6L8 8.4l3.7-2.8" fill="none" stroke="currentColor" stroke-width="0.9"/>
          </svg>
          Mark.Dolvery@brightlanecoverage.example
        </span>
      </div>
    </div>
  </section>

  <section class="card card-back" aria-label="Business card back">
    <div class="back-band"></div>
    <div class="logo">
      <span class="logo-dot"></span>
      <span class="logo-name">Brightlane Coverage</span>
    </div>
  </section>

</main>
</body>
</html>
```